Packaging label for launch of sun dried tomato products.

Established family farm in South Africa growing fruit for the production of dried fruit. We need a packaging label for the launch of our sun dried tomato products ie dried tomatoes in olive oil, dried tomato flakes and tomato powder. Packaging will be a round glass "jam jar" and spice shaker bottle. Due to limited amount of product available we cannot market to the masses, but rather focus on conveying a message of quality and exclusivity.

Target Market(s)

Home chef

Industry/Entity Type

Food

Font styles to use
Serif

Requirements
Nice to have
• Include the farm name in the design. TAVSONE

```html
<!DOCTYPE html>
<html lang="en">
<head>
<meta charset="utf-8">
<title>TAVSONE Sun Dried Tomato Labels</title>
<link rel="stylesheet" href="https://fonts.googleapis.com/css2?family=Fredoka:wght@600&family=Yellowtail&family=Montserrat:wght@800&family=Uncial+Antiqua&family=Oswald:wght@500;700&display=swap">
<style>
  :root{
    --bg:#efeeec;
    --cream:#fbecd4;
    --cream-ray:#f3dcb8;
    --brand-green:#2e9b48;
    --band-green:#2f9a45;
    --orange:#f29a1e;
    --tomato-red:#c8161e;
    --deep-red:#8e1016;
    --band-red:#d8261d;
    --sun-yellow:#f2c21c;
    --ink:#1d1d1b;
    --white:#ffffff;
  }
  *{box-sizing:border-box;margin:0;padding:0}
  html,body{width:1200px;height:900px;overflow:hidden;background:var(--bg)}
  .canvas{position:relative;width:1200px;height:900px}

  .label{position:absolute;overflow:hidden;
    background:radial-gradient(circle at 50% 45%, var(--cream) 0%, var(--cream) 35%, var(--cream-ray) 100%);
    box-shadow:0 6px 24px rgba(0,0,0,.12)}
  .label--jar{left:110px;top:150px;width:500px;height:580px}
  .label--shaker{left:690px;top:250px;width:320px;height:380px}

  .pattern-band{position:absolute;left:0;right:0}
  .pattern-band--diamond{top:0;background:linear-gradient(var(--band-red),var(--band-red)) center/100% 70% no-repeat,var(--ink)}
  .pattern-band--sun{bottom:0;background:var(--band-green);border-top:3px solid var(--sun-yellow)}
  .label--jar .pattern-band--diamond{height:40px}
  .label--jar .pattern-band--sun{height:62px}
  .label--shaker .pattern-band--diamond{height:22px}
  .label--shaker .pattern-band--sun{height:34px}

  .brand{position:absolute;text-align:center;white-space:nowrap;
    font-family:"Fredoka",sans-serif;font-weight:600;color:var(--brand-green);letter-spacing:.06em}
  .label--jar .brand{left:20px;width:390px;top:62px;font-size:48px}
  .label--shaker .brand{left:10px;width:260px;top:34px;font-size:30px}

  .product-script{position:absolute;text-align:center;white-space:nowrap;
    font-family:"Yellowtail","Brush Script MT",cursive;color:var(--orange);line-height:1}
  .label--jar .product-script{left:20px;width:390px;top:128px;font-size:86px;transform:rotate(-6deg)}
  .label--shaker .product-script{left:10px;width:260px;top:82px;font-size:46px;transform:rotate(-8deg)}

  .product-name{position:absolute;text-align:center;white-space:nowrap;font-family:"Montserrat",sans-serif;font-weight:800;
    color:var(--tomato-red);-webkit-text-stroke:2px var(--white);paint-order:stroke fill;line-height:1;z-index:2}
  .label--jar .product-name{left:88px;width:310px;top:262px;font-size:64px}
  .label--shaker .product-name{left:48px;width:190px;top:146px;font-size:38px;transform:rotate(-5deg)}

  .illustration{position:absolute}
  .label--jar .illustration{left:50px;top:240px;width:350px;height:240px;
    background:radial-gradient(ellipse at 35% 55%,#e8652a 0%,#c33a1c 45%,#7a1a12 80%,transparent 81%)}
  .label--shaker .illustration{left:70px;top:186px;width:160px;height:96px;
    background:radial-gradient(ellipse at 50% 50%,#d8631f 0%,#b4341a 50%,#5a2c1d 78%,transparent 80%)}

  .badges{position:absolute;display:flex;flex-direction:column;align-items:center}
  .label--jar .badges{right:12px;top:140px;gap:18px;width:70px}
  .label--shaker .badges{right:6px;top:110px;gap:10px;width:40px}
  .badge{display:flex;flex-direction:column;align-items:center;font-family:"Oswald",sans-serif;
    font-weight:500;color:var(--brand-green);text-align:center;line-height:1.1}
  .label--jar .badge{font-size:8px}
  .label--jar .badge svg{width:48px;height:48px;margin-bottom:4px}
  .label--shaker .badge{font-size:5px}
  .label--shaker .badge svg{width:26px;height:26px;margin-bottom:2px}

  .variant-box{position:absolute;left:78px;bottom:70px;width:330px;height:62px;background:var(--white);
    border:4px solid var(--brand-green);border-radius:10px;display:flex;align-items:center;justify-content:center;
    font-family:"Uncial Antiqua",serif;font-size:36px;color:var(--brand-green);z-index:3}

  .net-weight{position:absolute;font-family:"Oswald",sans-serif;white-space:nowrap}
  .label--jar .net-weight{left:-16px;top:450px;font-size:13px;font-weight:500;color:var(--ink);transform:rotate(90deg)}
  .label--shaker .net-weight{left:0;right:0;top:318px;text-align:center;font-size:14px;color:var(--tomato-red);font-weight:700}

  .ribbon{position:absolute;left:92px;top:268px;width:150px;height:36px;background:var(--tomato-red);
    border-radius:4px;transform:rotate(-4deg);display:flex;align-items:center;justify-content:center;
    font-family:"Oswald",sans-serif;font-weight:700;font-size:24px;color:var(--white);z-index:2}
  .ribbon::before{content:"";position:absolute;left:-16px;top:5px;width:20px;height:34px;background:var(--deep-red);z-index:-1}
</style>
</head>
<body>
<main class="canvas">

  <section class="label label--jar">
    <div class="pattern-band pattern-band--diamond" role="img" aria-label="Red and black diamond border pattern"></div>
    <div class="brand">TAVSONE</div>
    <div class="illustration" role="img" aria-label="Illustration of halved and sun dried tomatoes"></div>
    <div class="product-script">Sun Dried</div>
    <div class="product-name">TOMATO</div>
    <div class="badges">
      <div class="badge">
        <svg viewBox="0 0 48 48"><circle cx="24" cy="24" r="21" fill="none" stroke="currentColor" stroke-width="3"/><line x1="10" y1="38" x2="38" y2="10" stroke="currentColor" stroke-width="3"/><line x1="24" y1="14" x2="24" y2="36" stroke="currentColor" stroke-width="2"/></svg>
        GLUTEN FREE
      </div>
      <div class="badge">
        <svg viewBox="0 0 48 48"><circle cx="24" cy="24" r="21" fill="none" stroke="currentColor" stroke-width="3"/><path d="M14 24l7 8 13-16" fill="none" stroke="currentColor" stroke-width="4" stroke-linecap="round" stroke-linejoin="round"/></svg>
        100% VEGETARIAN
      </div>
      <div class="badge">
        <svg viewBox="0 0 48 48"><circle cx="24" cy="24" r="21" fill="none" stroke="currentColor" stroke-width="3"/><path d="M16 34C16 20 24 13 34 12C34 24 28 32 16 34Z" fill="currentColor"/></svg>
        ORGANIC FOOD
      </div>
    </div>
    <div class="net-weight">8 OZ (236G)</div>
    <div class="variant-box">in olive oil</div>
    <div class="pattern-band pattern-band--sun" role="img" aria-label="Green band with yellow sun spiral pattern"></div>
  </section>

  <section class="label label--shaker">
    <div class="pattern-band pattern-band--diamond" role="img" aria-label="Red and black diamond border pattern"></div>
    <div class="brand">TAVSONE</div>
    <div class="product-script">Sun Dried</div>
    <div class="illustration" role="img" aria-label="Photo of dried tomato flakes in a bowl"></div>
    <div class="product-name">TOMATO</div>
    <div class="badges">
      <div class="badge">
        <svg viewBox="0 0 48 48"><circle cx="24" cy="24" r="21" fill="none" stroke="currentColor" stroke-width="3"/><line x1="10" y1="38" x2="38" y2="10" stroke="currentColor" stroke-width="3"/><line x1="24" y1="14" x2="24" y2="36" stroke="currentColor" stroke-width="2"/></svg>
        GLUTEN FREE
      </div>
      <div class="badge">
        <svg viewBox="0 0 48 48"><circle cx="24" cy="24" r="21" fill="none" stroke="currentColor" stroke-width="3"/><path d="M14 24l7 8 13-16" fill="none" stroke="currentColor" stroke-width="4" stroke-linecap="round" stroke-linejoin="round"/></svg>
        100% VEGETARIAN
      </div>
      <div class="badge">
        <svg viewBox="0 0 48 48"><circle cx="24" cy="24" r="21" fill="none" stroke="currentColor" stroke-width="3"/><path d="M16 34C16 20 24 13 34 12C34 24 28 32 16 34Z" fill="currentColor"/></svg>
        ORGANIC FOOD
      </div>
    </div>
    <div class="ribbon">Flakes</div>
    <div class="net-weight">NET WT. 7 OZ (198 g)</div>
    <div class="pattern-band pattern-band--sun" role="img" aria-label="Green band with yellow sun spiral pattern"></div>
  </section>

</main>
</body>
</html>
```